New world-class investment firm needs a business card design

We need a business card design for a new investment firm called 'Dalvin Soeurs & Company.' We acquire companies in the media sector and secure funding from conservative ultra, high-net worth individuals. We would like a black and white color design. We are seeking classic, elegant, and sophisticated designs. The final design should communicate financial safety, class, timelessness, and highly ethical. On the back of the business card, we would simply like the lion logo to be centered. I have attached a mock card, and variations on it are welcomed.
Industry/Entity Type
Conservative
Font styles to use
Other font styles liked:
- Garamond
Look and feel
Each slider illustrates characteristics of the customer's brand and the style your logo design should communicate.

```html
<!DOCTYPE html>
<html lang="en">
<head>
<meta charset="utf-8">
<title>Dalvin Soeurs &amp; Company — Business Card</title>
<link rel="stylesheet" href="https://fonts.googleapis.com/css2?family=Lato:wght@400;700;900&display=swap">
<style>
  :root {
    --backdrop: #2b2b2b;
    --card: #ffffff;
    --card-shade: #f1f1f1;
    --ink: #141414;
    --muted: #8a8a8a;
    --faint: #dedede;
  }
  * { margin: 0; padding: 0; box-sizing: border-box; }
  html, body {
    width: 1200px; height: 900px; overflow: hidden;
    background: var(--backdrop);
    font-family: "Lato", Arial, sans-serif;
    color: var(--ink);
  }
  .canvas { position: relative; width: 1200px; height: 900px; }

  .card {
    position: absolute;
    width: 600px; height: 343px;
    background: linear-gradient(160deg, var(--card) 0%, var(--card) 55%, var(--card-shade) 100%);
    box-shadow: 0 10px 30px rgba(0,0,0,.45);
    overflow: hidden;
  }

  /* Back of card: centred mark only */
  .card-back { left: 60px; top: 70px; }
  .back-mark {
    position: absolute; left: 50%; top: 50%;
    transform: translate(-50%, -50%);
    width: 270px; height: 270px; border-radius: 50%;
    border: 6px solid var(--ink);
    display: flex; align-items: center; justify-content: center;
    text-align: center; padding: 34px;
    font-weight: 900; font-size: 26px; line-height: 1.2;
    text-transform: uppercase; letter-spacing: .5px;
  }

  /* Front of card */
  .card-front { left: 560px; top: 480px; }
  .watermark {
    position: absolute; right: 14px; top: 100px;
    width: 226px; height: 226px; border-radius: 50%;
    border: 6px solid var(--faint);
    display: flex; align-items: center; justify-content: center;
    text-align: center;
    color: var(--faint); font-weight: 900; font-size: 20px;
    text-transform: uppercase; line-height: 1.2; padding: 28px;
  }
  .holder { position: absolute; right: 26px; top: 26px; text-align: right; }
  .holder-name { font-weight: 900; font-size: 17px; text-transform: uppercase; letter-spacing: .3px; }
  .holder-title { font-weight: 700; font-size: 13px; color: var(--muted); text-transform: uppercase; letter-spacing: .6px; }

  .firm { position: absolute; left: 26px; top: 40px; }
  .firm-circle {
    width: 112px; height: 112px; border-radius: 50%;
    border: 4px solid var(--ink);
  }
  .firm-name {
    margin-top: 12px;
    font-weight: 900; font-size: 24px; text-transform: uppercase; letter-spacing: .2px;
  }
  .firm-cities { font-weight: 700; font-size: 16px; margin-top: 1px; }

  .contact { position: absolute; left: 26px; bottom: 24px; list-style: none; }
  .contact li { display: flex; align-items: center; gap: 10px; font-weight: 700; font-size: 15px; margin-top: 9px; }
  .contact svg { width: 16px; height: 16px; flex: none; }
  .contact .web { color: var(--muted); font-size: 17px; font-weight: 900; margin-top: 10px; }
</style>
</head>
<body>
<main class="canvas">

  <section class="card card-back" aria-label="Card back">
    <div class="back-mark">Dalvin Soeurs &amp; Company</div>
  </section>

  <section class="card card-front" aria-label="Card front">
    <div class="watermark" aria-hidden="true">Dalvin Soeurs &amp; Company</div>

    <div class="holder">
      <p class="holder-name">Elias T. Varnum</p>
      <p class="holder-title">Chairman &amp; CEO</p>
    </div>

    <div class="firm">
      <div class="firm-circle"></div>
      <h1 class="firm-name">Dalvin Soeurs &amp; Company</h1>
      <p class="firm-cities">New York • Los Angles • Geneva</p>
    </div>

    <ul class="contact">
      <li>
        <svg viewBox="0 0 16 16" aria-hidden="true"><path d="M2 5c0-2 2-3 6-3s6 1 6 3v1h-3V5H5v1H2z M4 7h8l2 6H2z" fill="#141414"/><circle cx="8" cy="10" r="1.6" fill="#fff"/></svg>
        212.555.0148
      </li>
      <li>
        <svg viewBox="0 0 16 16" aria-hidden="true"><rect x="1" y="3" width="14" height="10" fill="#141414"/><path d="M1.5 3.5 8 9l6.5-5.5" fill="none" stroke="#fff" stroke-width="1.2"/></svg>
        elias@dalvinsoeurs.com
      </li>
      <li class="web">www.dalvinsoeurs.com</li>
    </ul>
  </section>

</main>
</body>
</html>
```